LUMEN Environmental needs an upgrade to its current business cards design

We need an upgrade to our current business cards design, where the LUMEN acronym is included, as possible and not being overloaded.
LUMEN Environmental is an Environmental Consultancy Firm based in Sydney.
We would like to see creative designs different from the standard type of business cards (for example, rounded edges, different to standard size of common business cards.

Target Market(s)

industrial companies (oil & gas, petrochemical, mining, insolvency, finance and manufacturing), developers, architect firms, law firms.

Industry/Entity Type

Business

Contact Information for Business Card

logos (brand and acronym), if they don't appear overloaded.
name
role
name of company (LUMEN Environmental),
address (Level 4, Suite 4B, 72-76 Wrenfield Street, Marlow Vale, NSW, 2093) landline (02 7314 2286)
mobile (staff member)
email (staff member) and
website (www.lumenverda.example).
Include: Contaminated Land, Site Remediation, Groundwater Assessment, Health and Ecological Risk Assessments, Acid Sulfate Soils, Waste Classification.

Font styles to use
Serif
Sans Serif

Requirements
Must have
• A creative design different to the standard type of business cards.
Nice to have
• Rounded edges
• Different size of business cards rather than the standard size.
Should not have
• Preferable not to use white colour background, unless it is required from a creative design proposed.
• Not an overloaded design.
• Avoid black colours

```html
<!DOCTYPE html>
<html lang="en">
<head>
<meta charset="utf-8">
<title>LUMEN Environmental – Business Card</title>
<link rel="stylesheet" href="https://fonts.googleapis.com/css2?family=Open+Sans:wght@400;600;800&display=swap">
<style>
  :root {
    --backdrop: #3b3b3d;
    --card-dark: #121212;
    --card-dark-edge: #262626;
    --lime: #8cc63f;
    --lime-soft: #a6d15a;
    --panel-top: #8fb05a;
    --panel-bottom: #4a4a4a;
    --text-light: #f2f2f2;
    --text-muted: #bdbdbd;
    --outline: #ffffff;
  }
  * { margin: 0; padding: 0; box-sizing: border-box; }
  html, body { width: 1200px; height: 950px; overflow: hidden; }
  body {
    background: var(--backdrop);
    font-family: "Open Sans", Arial, sans-serif;
    position: relative;
  }
  .card {
    position: absolute;
    left: 240px;
    width: 720px;
    height: 400px;
    border-radius: 14px;
    overflow: hidden;
    background: linear-gradient(120deg, var(--card-dark-edge) 0%, var(--card-dark) 55%, #1c1c1c 100%);
    box-shadow: 0 10px 30px rgba(0,0,0,0.45);
  }
  .card--back { top: 45px; }
  .card--front { top: 505px; }

  .wordmark {
    color: var(--lime);
    font-weight: 800;
    line-height: 1;
    white-space: nowrap;
  }
  .wordmark__name { display: block; font-size: 92px; letter-spacing: 4px; }
  .wordmark__sub { display: block; font-size: 25px; letter-spacing: 9px; margin-top: 4px; }

  .card--back .wordmark { position: absolute; left: 180px; top: 70px; }
  .services {
    position: absolute;
    left: 180px;
    top: 245px;
    color: var(--text-muted);
    font-size: 16px;
    line-height: 1.65;
    list-style: none;
    white-space: nowrap;
  }
  .services .dot { color: var(--lime); margin: 0 6px; }

  .step-panel { position: absolute; inset: 0; }
  .card--front .wordmark { position: absolute; left: 450px; top: 128px; }
  .card--front .wordmark__name { font-size: 62px; letter-spacing: 3px; }
  .card--front .wordmark__sub { font-size: 17px; letter-spacing: 6px; margin-top: 6px; }

  .contact {
    position: absolute;
    left: 34px;
    top: 34px;
    color: var(--text-light);
    font-size: 17px;
    line-height: 1.35;
  }
  .contact__name { color: var(--lime-soft); font-size: 20px; font-weight: 600; letter-spacing: 1px; }
  .contact__role { font-size: 18px; letter-spacing: 1px; margin-bottom: 30px; }
  .contact__company { font-weight: 600; }
  .contact__address { margin-bottom: 16px; }
  .contact__row { display: flex; align-items: center; gap: 10px; }
  .contact__row svg { width: 15px; height: 15px; fill: var(--lime); flex: none; }
</style>
</head>
<body>

<section class="card card--back" aria-label="Card back">
  <div class="wordmark">
    <span class="wordmark__name">LUMEN</span>
    <span class="wordmark__sub">ENVIRONMENTAL</span>
  </div>
  <ul class="services">
    <li>Contaminated Land<span class="dot">•</span>Site Remediation<span class="dot">•</span>Groundwater Assessment</li>
    <li>Health &amp; Ecological Risk Assessments<span class="dot">•</span>Acid Sulfate Soils</li>
    <li>Waste Classification.</li>
  </ul>
</section>

<section class="card card--front" aria-label="Card front">
  <svg class="step-panel" viewBox="0 0 720 400" width="720" height="400" aria-hidden="true">
    <defs>
      <linearGradient id="panelFill" x1="0" y1="0" x2="0" y2="1">
        <stop offset="0" stop-color="#8fb05a"/>
        <stop offset="1" stop-color="#4a4a4a"/>
      </linearGradient>
    </defs>
    <polygon fill="url(#panelFill)" stroke="#ffffff" stroke-width="3"
      points="-5,-5 290,-5 290,70 325,70 325,150 360,150 360,230 395,230 395,310 430,310 430,405 -5,405"/>
  </svg>

  <div class="contact">
    <div class="contact__name">ALEX MARLO</div>
    <div class="contact__role">PRESIDENT</div>
    <div class="contact__company">LUMEN Environmental</div>
    <div class="contact__address">Level 4, Suite 4B<br>72-76 Wrenfield Street<br>Marlow Vale, NSW, 2093</div>
    <div class="contact__row">
      <svg viewBox="0 0 16 16"><path d="M3 1h3l1.5 4-2 1.2a9 9 0 0 0 4.3 4.3L11 8.5l4 1.5v3c0 1-1 2-2 2A13 13 0 0 1 1 3c0-1 1-2 2-2z"/></svg>
      <span>02 7314 2286</span>
    </div>
    <div class="contact__row">
      <svg viewBox="0 0 16 16"><path d="M4 0h8a1 1 0 0 1 1 1v14a1 1 0 0 1-1 1H4a1 1 0 0 1-1-1V1a1 1 0 0 1 1-1zm1 2v10h6V2z"/></svg>
      <span>0412 555 018</span>
    </div>
    <div class="contact__row">
      <svg viewBox="0 0 16 16"><path d="M0 3h16v2L8 10 0 5zm0 4 8 5 8-5v6H0z"/></svg>
      <span>name@lumenverda.example</span>
    </div>
    <div class="contact__row">
      <svg viewBox="0 0 16 16"><circle cx="8" cy="8" r="7.5"/></svg>
      <span>www.lumenverda.example</span>
    </div>
  </div>

  <div class="wordmark">
    <span class="wordmark__name">LUMEN</span>
    <span class="wordmark__sub">ENVIRONMENTAL</span>
  </div>
</section>

</body>
</html>
```